Business cards for financial advisor-insurance agent firm

Our company, Harlow Pemberton Insurance & Investments, is an insurance (health, life, home, auto, etc) and investment brokerage offering a suite of options to meet client needs. We need business cards that are professional and embody strength, security and sophistication.

Also running a letterhead project at
http://jobs.briefmarlo.com/job.aspx?id=519087

Target Market(s)

Upper middle class and wealthy

Industry/Entity Type

Investment

Requirements
Nice to have
• Looking for either white, navy blue, or gray cards

```html
<!DOCTYPE html>
<html lang="en">
<head>
<meta charset="utf-8">
<title>Harlow Pemberton Insurance &amp; Investments – Business Cards</title>
<link href="https://fonts.googleapis.com/css2?family=Cinzel:wght@500&family=Open+Sans:wght@400;700&display=swap" rel="stylesheet">
<style>
  :root{
    --stage:#3b3c3f;
    --navy:#262d55;
    --navy-light:#333b68;
    --slate:#6f828e;
    --ink:#2c3153;
    --text:#3d3d3d;
    --white:#ffffff;
  }
  *{margin:0;padding:0;box-sizing:border-box}
  html,body{width:1200px;height:946px;overflow:hidden;background:var(--stage)}
  .sheet{position:relative;width:1200px;height:946px}
  .card{position:absolute;left:215px;width:770px;height:440px;overflow:hidden;box-shadow:0 10px 28px rgba(0,0,0,.45)}
  .card-back{top:22px;background:radial-gradient(ellipse at 42% 40%,var(--navy-light) 0%,var(--navy) 60%)}
  .card-front{top:484px;background:var(--white)}

  .brand{position:absolute;display:flex;flex-direction:column;align-items:center;font-family:"Cinzel",serif;font-weight:500}
  .brand-mark{width:62px;height:62px;border:3px solid currentColor;margin-bottom:14px}
  .brand-name{font-size:36px;letter-spacing:1px;line-height:1;white-space:nowrap}
  .brand-tag{font-size:15px;letter-spacing:2px;margin-top:6px;white-space:nowrap}

  .card-back .brand{left:0;right:0;top:128px;color:var(--white)}
  .back-url{position:absolute;right:44px;bottom:34px;color:var(--white);font:400 15px "Open Sans",sans-serif}

  .card-front .brand{left:60px;width:420px;top:60px;color:var(--ink)}
  .card-front .brand-name{font-size:32px}
  .card-front .brand-tag{font-size:14px}
  .divider{position:absolute;left:230px;top:232px;width:496px;height:1px;background:var(--ink)}
  .address{position:absolute;right:44px;top:112px;text-align:right;font:400 16px/1.35 "Open Sans",sans-serif;color:var(--text);white-space:nowrap}

  .contact{position:absolute;left:48px;top:250px;font-family:"Open Sans",sans-serif;color:var(--text)}
  .contact-name{font-weight:700;font-size:19px;color:var(--slate);letter-spacing:.5px}
  .contact-role{font-size:14px;margin-bottom:10px}
  .contact-line{display:flex;align-items:center;gap:9px;font-size:16px;line-height:22px}
  .contact-line svg{width:14px;height:14px;fill:var(--ink)}

  .front-bands{position:absolute;left:0;bottom:0}
  .front-url{position:absolute;right:36px;bottom:18px;color:var(--white);font:400 15px "Open Sans",sans-serif}
</style>
</head>
<body>
<div class="sheet">

  <section class="card card-back" aria-label="Card back">
    <div class="brand">
      <span class="brand-mark"></span>
      <span class="brand-name">Harlow Pemberton</span>
      <span class="brand-tag">Insurance &amp; Investments</span>
    </div>
    <p class="back-url">www.wesitename.com</p>
  </section>

  <section class="card card-front" aria-label="Card front">
    <div class="brand">
      <span class="brand-mark"></span>
      <span class="brand-name">Harlow Pemberton</span>
      <span class="brand-tag">Insurance &amp; Investments</span>
    </div>
    <div class="divider"></div>
    <p class="address">Your address Goes Here,<br>Street Name, City,<br>Zip Code, Country Name</p>

    <div class="contact">
      <p class="contact-name">MILES CARTER</p>
      <p class="contact-role">CEO</p>
      <p class="contact-line"><svg viewBox="0 0 16 16"><path d="M3 1l3 3-2 2c1 2 3 4 5 5l2-2 3 3-2 3C6 15 1 10 1 3z"/></svg>555 210 4839</p>
      <p class="contact-line"><svg viewBox="0 0 16 16"><path d="M4 0h8v16H4zM5.5 1.5v11h5v-11zM7 13.5h2v1H7z" fill-rule="evenodd"/></svg>555 386 9021</p>
      <p class="contact-line"><svg viewBox="0 0 16 16"><path d="M0 3h16v10H0zM1 4l7 5 7-5v1L8 10 1 5z"/></svg>name@domainname.com</p>
    </div>

    <svg class="front-bands" width="770" height="120" viewBox="0 0 770 120" aria-hidden="true">
      <polygon points="0,58 560,58 600,22 770,22 770,30 604,30 564,66 0,66" fill="var(--navy)"/>
      <polygon points="0,74 568,74 608,38 770,38 770,120 0,120" fill="var(--slate)"/>
      <polygon points="0,100 600,100 630,70 770,70 770,120 0,120" fill="var(--navy)"/>
    </svg>
    <p class="front-url">www.wesitename.com</p>
  </section>

</div>
</body>
</html>
```